Brilliant Design Needed For Stand Up Pouch - Drink Mix

We need a layout for our resealable stand-up pouch that holds our powered sports drink mix. Target audience is endurance athletes that enjoy marathon running, cycling, mountain biking, hiking and triathlon. Secondary audience are participants in team sports such soccer, lacrosse, football and basketball. Please review the attached project brief for full details. Thanks!

Target Market(s)

50/50 male/female, ages 20-50, USA, succesful, driven, educated. Active, healthy, athletic, outdoor lifestyle.

Industry/Entity Type

Fitness

Font styles to use
Sans Serif

Colors
33a6d7
3277b5
abd037

Requirements
Must have
• Please review the attached project brief for full details.
Nice to have
Should not have

```html
<!DOCTYPE html>
<html lang="en">
<head>
<meta charset="utf-8">
<title>Stridewell Hydration Drink Mix Pouch</title>
<link rel="stylesheet" href="https://fonts.googleapis.com/css2?family=Source+Sans+3:wght@400;600;700;800&display=swap">
<style>
  :root {
    --page-bg: #f1efe2;
    --blue-deep: #1c4ea3;
    --blue-mid: #2a6fc4;
    --brand-blue: #3277b5;
    --sky: #33a6d7;
    --sky-light: #5cc3ea;
    --lime: #abd037;
    --lime-dark: #6f9a22;
    --lemon: #f3d43a;
    --lemon-light: #fbeea0;
    --white: #ffffff;
    --ink-blue: #1d4c8f;
  }
  * { margin: 0; padding: 0; box-sizing: border-box; }
  html, body {
    width: 1200px;
    height: 1020px;
    overflow: hidden;
    background: var(--page-bg);
    font-family: "Source Sans 3", Arial, sans-serif;
  }
  .pouch {
    position: absolute;
    left: 320px;
    top: 110px;
    width: 560px;
    height: 800px;
  }
  .pouch-shape { position: absolute; inset: 0; }
  .pouch-text { position: absolute; color: var(--white); white-space: nowrap; }

  .product-type { left: 63px; top: 160px; font-size: 38px; font-weight: 700; line-height: 1; }
  .product-subtitle { left: 64px; top: 202px; font-size: 15px; font-weight: 400; color: #d9e8fb; }

  .duration-tag {
    left: 300px; top: 138px; width: 188px; height: 94px;
    background: var(--sky-light);
    transform: rotate(-3deg);
    display: flex; align-items: center; justify-content: center; text-align: center;
    font-size: 23px; font-weight: 700; line-height: 1.15; white-space: normal;
  }

  .brand-name {
    left: 0; width: 560px; top: 384px; text-align: center;
    font-size: 58px; font-weight: 800; letter-spacing: 1px;
    color: var(--brand-blue);
    display: flex; align-items: center; justify-content: center; gap: 14px;
  }
  .brand-dot { width: 22px; height: 22px; border-radius: 50%; background: var(--sky); }

  .line-name { left: 70px; top: 500px; font-size: 30px; font-weight: 700; color: var(--brand-blue); }
  .line-tag {
    left: 78px; top: 536px; padding: 2px 12px;
    background: var(--brand-blue); font-size: 12px; font-weight: 600;
    transform: rotate(-4deg);
  }

  .lemon-photo {
    position: absolute; left: 62px; top: 560px; width: 200px; height: 126px;
    border-radius: 60px;
    background: radial-gradient(ellipse at 35% 45%, var(--lemon-light), var(--lemon) 70%);
  }

  .flavor { left: 318px; top: 598px; transform: rotate(-5deg); transform-origin: left top; }
  .flavor-name { font-size: 26px; font-weight: 700; line-height: 1; }
  .flavor-note { font-size: 16px; font-weight: 400; line-height: 1.2; }

  .formula-number { left: 52px; top: 690px; font-size: 58px; font-weight: 800; line-height: 1; }
  .formula-name { left: 102px; top: 698px; font-size: 32px; font-weight: 700; line-height: 1; }
  .formula-note {
    left: 102px; top: 732px; width: 400px; height: 22px; padding-left: 6px;
    background: var(--white); color: var(--ink-blue);
    font-size: 14px; font-weight: 600; line-height: 22px;
  }
  .servings { left: 42px; top: 756px; font-size: 10px; line-height: 1.15; color: #dbe8fb; }
  .net-weight { left: 368px; top: 768px; font-size: 11px; color: #dbe8fb; }
</style>
</head>
<body>
  <div class="pouch">
    <svg class="pouch-shape" viewBox="0 0 560 800" width="560" height="800" aria-hidden="true">
      <defs>
        <linearGradient id="bagBlue" x1="0" y1="0" x2="1" y2="1">
          <stop offset="0" stop-color="#2a6fc4"/>
          <stop offset="1" stop-color="#1c4ea3"/>
        </linearGradient>
        <linearGradient id="headerBlue" x1="0" y1="0" x2="0" y2="1">
          <stop offset="0" stop-color="#2463ba"/>
          <stop offset="1" stop-color="#3a86d2"/>
        </linearGradient>
        <linearGradient id="limeBand" x1="0" y1="0" x2="1" y2="0">
          <stop offset="0" stop-color="#abd037"/>
          <stop offset="1" stop-color="#6f9a22"/>
        </linearGradient>
      </defs>
      <path class="pouch-body" fill="url(#bagBlue)"
        d="M18,0 H542 Q560,0 560,18 V92 A8,8 0 0 0 560,108 V782 Q560,800 542,800 H18 Q0,800 0,782 V108 A8,8 0 0 0 0,92 V18 Q0,0 18,0 Z"/>
      <rect class="hang-hole" x="225" y="26" width="110" height="24" rx="12" fill="#f1efe2"/>
      <path class="front-panel" fill="#ffffff"
        d="M37,114 Q37,82 69,82 H491 Q523,82 523,114 V610 H37 Z"/>
      <path class="panel-header" fill="url(#headerBlue)"
        d="M37,114 Q37,82 69,82 H491 Q523,82 523,114 V248 Q280,262 37,250 Z"/>
      <polygon class="flavor-band" fill="url(#limeBand)" points="37,592 523,570 523,650 37,702"/>
      <polygon class="lower-band" fill="url(#bagBlue)" points="37,702 523,650 523,800 37,800"/>
    </svg>

    <div class="pouch-text product-type">Drink Mix</div>
    <div class="pouch-text product-subtitle">Advanced Hydration System</div>
    <div class="pouch-text duration-tag">Hydration by Duration</div>

    <div class="pouch-text brand-name"><span class="brand-dot"></span>STRIDEWELL</div>

    <div class="pouch-text line-name">HYDRATION</div>
    <div class="pouch-text line-tag">Endurance Formula</div>

    <div class="lemon-photo" role="img" aria-label="Photo of a whole lemon and a lemon slice"></div>

    <div class="pouch-text flavor">
      <div class="flavor-name">Lemon-Lime</div>
      <div class="flavor-note">With other natural flavors</div>
    </div>

    <div class="pouch-text formula-number">2</div>
    <div class="pouch-text formula-name">ENDURANCE FORMULA</div>
    <div class="pouch-text formula-note">Recommended for workouts lasting 2 hour</div>
    <div class="pouch-text servings">Makes 27<br>12 fl oz Serving</div>
    <div class="pouch-text net-weight">NET WT 15.5 OZ (440G)</div>
  </div>
</body>
</html>
```